Educational outcome management software startup firm needs a graphic design

Our software startup firm, Pelvar Insight Technologies recently purchased a beautiful logo from Brushmarket (uploaded file). We are now looking for a graphic design to be used in the marketing activities of Pelvar Insight Technologies. See the uploaded picture of what a sketch of the graphic we are looking for.

```html
<!DOCTYPE html>
<html lang="en">
<head>
<meta charset="utf-8">
<title>Learner Wheel of Success – Pelvar Insight Technologies</title>
<link rel="stylesheet" href="https://fonts.googleapis.com/css2?family=Oswald:wght@500;600&family=Poppins:wght@500;600&display=swap">
<style>
  :root {
    --navy: #1d3461;
    --red: #d0433a;
    --header-grey: #e7e7e8;
    --poster-white: #ffffff;
    --page-bg: #eeeeef;
    --label-ink: #1d3461;
  }
  html, body {
    margin: 0;
    padding: 0;
    width: 1200px;
    height: 2400px;
    overflow: hidden;
    background: var(--page-bg);
  }
  .poster {
    position: absolute;
    left: 0;
    top: 654px;
    width: 1200px;
    height: 1091px;
    display: block;
    filter: drop-shadow(0 6px 14px rgba(0,0,0,0.18));
  }
  .poster-sheet { fill: var(--poster-white); }
  .header-band { fill: var(--header-grey); }
  .brand-name {
    font-family: "Poppins", sans-serif;
    font-weight: 600;
    fill: var(--navy);
  }
  .brand-square { fill: var(--red); }
  .title-small {
    font-family: "Oswald", sans-serif;
    font-weight: 600;
    font-size: 48px;
    fill: var(--navy);
  }
  .title-large {
    font-family: "Oswald", sans-serif;
    font-weight: 600;
    font-size: 114px;
    fill: var(--red);
  }
  .slice-red { fill: var(--red); stroke: #fff; stroke-width: 2.5; }
  .slice-navy { fill: var(--navy); stroke: #fff; stroke-width: 2.5; }
  .skills-ring { fill: var(--red); stroke: #fff; stroke-width: 4; }
  .skills-divider { stroke: #fff; stroke-width: 2; }
  .hub { fill: #fff; }
  .orbit { fill: none; stroke: var(--navy); stroke-width: 3; stroke-dasharray: 11 7; }
  .node { fill: var(--navy); stroke: var(--red); stroke-width: 3.5; }
  .node-ring { fill: none; stroke: #fff; stroke-width: 1.5; }
  .icon-spot { fill: #ffffff; opacity: 0.9; }
  .icon-spot-hub { fill: var(--red); }
  .segment-label, .skill-label {
    font-family: "Poppins", sans-serif;
    font-weight: 500;
    font-size: 11px;
    fill: #fff;
    text-anchor: middle;
  }
  .hub-label {
    font-family: "Poppins", sans-serif;
    font-weight: 600;
    font-size: 14px;
    fill: var(--navy);
    text-anchor: middle;
  }
  .node-label {
    font-family: "Poppins", sans-serif;
    font-weight: 600;
    font-size: 11px;
    fill: var(--label-ink);
  }
  .footer-band { fill: var(--red); }
</style>
</head>
<body>
<svg class="poster" viewBox="0 0 1065 968" xmlns="http://www.w3.org/2000/svg" aria-label="Learner Wheel of Success poster">
  <rect class="poster-sheet" x="0" y="0" width="1065" height="968"/>

  <!-- Header -->
  <path class="header-band" d="M36 0 H1028 V138 A50 50 0 0 1 978 188 H86 A50 50 0 0 1 36 138 Z"/>
  <g class="brand">
    <rect class="brand-square" x="98" y="80" width="22" height="22"/>
    <text class="brand-name" x="132" y="91" font-size="27">Pelvar Insight</text>
    <text class="brand-name" x="132" y="121" font-size="27">Technologies</text>
  </g>
  <g class="title">
    <text class="title-small" x="466" y="98" textLength="160" lengthAdjust="spacingAndGlyphs">LEARNER</text>
    <text class="title-small" x="466" y="143" textLength="160" lengthAdjust="spacingAndGlyphs">WHEEL OF</text>
    <text class="title-large" x="648" y="143" textLength="328" lengthAdjust="spacingAndGlyphs">SUCCESS</text>
  </g>

  <!-- Wheel -->
  <g class="wheel">
    <circle class="orbit" cx="531" cy="563" r="287"/>

    <path class="slice-red"  d="M531 563 L349.3 381.3 A257 257 0 0 1 712.7 381.3 Z"/>
    <path class="slice-navy" d="M531 563 L712.7 381.3 A257 257 0 0 1 788 563 Z"/>
    <path class="slice-red"  d="M531 563 L788 563 A257 257 0 0 1 712.7 744.7 Z"/>
    <path class="slice-navy" d="M531 563 L712.7 744.7 A257 257 0 0 1 349.3 744.7 Z"/>
    <path class="slice-red"  d="M531 563 L349.3 744.7 A257 257 0 0 1 274 563 Z"/>
    <path class="slice-navy" d="M531 563 L274 563 A257 257 0 0 1 349.3 381.3 Z"/>

    <circle class="skills-ring" cx="531" cy="563" r="134"/>
    <g class="skills-dividers">
      <line class="skills-divider" x1="483" y1="515" x2="436.2" y2="468.2"/>
      <line class="skills-divider" x1="579" y1="515" x2="625.8" y2="468.2"/>
      <line class="skills-divider" x1="599" y1="563" x2="665" y2="563"/>
      <line class="skills-divider" x1="579" y1="611" x2="625.8" y2="657.8"/>
      <line class="skills-divider" x1="483" y1="611" x2="436.2" y2="657.8"/>
      <line class="skills-divider" x1="463" y1="563" x2="397" y2="563"/>
    </g>
    <circle class="hub" cx="531" cy="563" r="68"/>

    <!-- Segment icons and labels -->
    <circle class="icon-spot" cx="531" cy="337" r="13" role="img" aria-label="Graduation cap and diploma icon"/>
    <text class="segment-label" x="531" y="373">HIGH SCHOOL</text>
    <text class="segment-label" x="531" y="387">GRADUATION</text>

    <circle class="icon-spot" cx="352" cy="465" r="13" role="img" aria-label="Entrepreneur in suit icon"/>
    <text class="segment-label" x="350" y="499">ENTREPRENEUR</text>

    <circle class="icon-spot" cx="706" cy="465" r="13" role="img" aria-label="Employee with hard hat icon"/>
    <text class="segment-label" x="717" y="499">EMPLOYMENT</text>

    <circle class="icon-spot" cx="362" cy="600" r="13" role="img" aria-label="Graduate in cap and gown icon"/>
    <text class="segment-label" x="363" y="655">GRADUATION</text>
    <text class="segment-label" x="363" y="669">FROM</text>
    <text class="segment-label" x="363" y="683">HIGHER</text>
    <text class="segment-label" x="363" y="697">EDUCATION</text>

    <circle class="icon-spot" cx="700" cy="603" r="13" role="img" aria-label="Application form and pen icon"/>
    <text class="segment-label" x="697" y="651">ADMISSION</text>
    <text class="segment-label" x="697" y="665">INTO</text>
    <text class="segment-label" x="697" y="679">POST-SECONDARY</text>
    <text class="segment-label" x="697" y="693">INSTITUTION</text>

    <circle class="icon-spot" cx="529" cy="737" r="13" role="img" aria-label="School building icon"/>
    <text class="segment-label" x="529" y="771">COMPLETION OF</text>
    <text class="segment-label" x="529" y="785">ELEMENTARY</text>
    <text class="segment-label" x="529" y="799">SCHOOL</text>

    <!-- Skills labels -->
    <text class="skill-label" x="530" y="464">READING</text>
    <text class="skill-label" x="530" y="478">SKILLS</text>
    <text class="skill-label" x="614" y="510">WRITING</text>
    <text class="skill-label" x="614" y="524">SKILLS</text>
    <text class="skill-label" x="443" y="512">STEM</text>
    <text class="skill-label" x="443" y="526">SKILLS</text>
    <text class="skill-label" x="441" y="618">SOCIAL</text>
    <text class="skill-label" x="441" y="632">SKILLS</text>
    <text class="skill-label" x="618" y="618">STUDY</text>
    <text class="skill-label" x="618" y="632">SKILLS</text>
    <text class="skill-label" x="532" y="653">INFORMATION</text>
    <text class="skill-label" x="532" y="667">TECHNOLOGY</text>
    <text class="skill-label" x="532" y="681">SKILLS</text>

    <!-- Hub -->
    <circle class="icon-spot-hub" cx="531" cy="537" r="13" role="img" aria-label="Student reading a book icon"/>
    <text class="hub-label" x="531" y="585">LEARNER/</text>
    <text class="hub-label" x="531" y="601">STUDENT</text>

    <!-- Stakeholder nodes -->
    <g class="stakeholder">
      <circle class="node" cx="530" cy="258" r="27"/>
      <circle class="node-ring" cx="530" cy="258" r="12" role="img" aria-label="Parent and child icon"/>
      <text class="node-label" x="530" y="223" text-anchor="middle">PARENT/GUARDIAN</text>
    </g>
    <g class="stakeholder">
      <circle class="node" cx="305" cy="358" r="27"/>
      <circle class="node-ring" cx="305" cy="358" r="12" role="img" aria-label="Teacher at board icon"/>
      <text class="node-label" x="264" y="363" text-anchor="end">TEACHER</text>
    </g>
    <g class="stakeholder">
      <circle class="node" cx="757" cy="353" r="27"/>
      <circle class="node-ring" cx="757" cy="353" r="12" role="img" aria-label="Employer with briefcase icon"/>
      <text class="node-label" x="794" y="358">EMPLOYER</text>
    </g>
    <g class="stakeholder">
      <circle class="node" cx="228" cy="562" r="27"/>
      <circle class="node-ring" cx="228" cy="562" r="12" role="img" aria-label="Counselor at desk icon"/>
      <text class="node-label" x="155" y="560" text-anchor="middle">SCHOOL</text>
      <text class="node-label" x="155" y="574" text-anchor="middle">COUNSELOR</text>
    </g>
    <g class="stakeholder">
      <circle class="node" cx="836" cy="562" r="27"/>
      <circle class="node-ring" cx="836" cy="562" r="12" role="img" aria-label="College building icon"/>
      <text class="node-label" x="923" y="554" text-anchor="middle">POST-SECONDARY</text>
      <text class="node-label" x="923" y="568" text-anchor="middle">EDUCATION</text>
      <text class="node-label" x="923" y="582" text-anchor="middle">SYSTEMS</text>
    </g>
    <g class="stakeholder">
      <circle class="node" cx="303" cy="770" r="27"/>
      <circle class="node-ring" cx="303" cy="770" r="12" role="img" aria-label="Administrator with gear icon"/>
      <text class="node-label" x="218" y="758" text-anchor="middle">SCHOOL</text>
      <text class="node-label" x="218" y="772" text-anchor="middle">ADMINISTRATOR</text>
    </g>
    <g class="stakeholder">
      <circle class="node" cx="758" cy="762" r="27"/>
      <circle class="node-ring" cx="758" cy="762" r="12" role="img" aria-label="Government building icon"/>
      <text class="node-label" x="796" y="766">GOVERNMENT</text>
    </g>
    <g class="stakeholder">
      <circle class="node" cx="531" cy="865" r="27"/>
      <circle class="node-ring" cx="531" cy="865" r="12" role="img" aria-label="Global exchange icon"/>
      <text class="node-label" x="529" y="910" text-anchor="middle">INTERNATION MARKET PLACE</text>
    </g>
  </g>

  <!-- Footer band -->
  <path class="footer-band" d="M145 968 Q160 948 200 948 H863 Q903 948 918 968 Z"/>
</svg>
</body>
</html>
```